Catholic Musical composer/producer needs poster for groundbreaking new musical, "Harvest of Velmont

We need a dynamic poster for "Harvest of Velmont," a new musical written for Lantern Table Stage. Looking for that iconic poster graphic like you see in posters for classic musicals, like "Nuit Dorée," Carousel of Lanterns," or "Spindle."
***

"Harvest of Velmont" is based on the Gospel of John 2:1-11 where Jesus performs his first miracle at the behest of His Mother, Mary. It takes place at a wedding where the host family runs out of wine, a huge embarrassment. Mary becomes aware of the problem and directs Jesus to intercede. Jesus directs the wine steward to fill 6 large 30 gallon jars with water. He prays over them, turning the water into wine. The chalice of wine is a symbol for the Eucharist (communion). Even more, the Blood of Christ (the wine) is the source of spiritual life. Poster text is found on attachment.

Target Market(s)

The audience is adult members of Catholic churches. Don't want design to look too "churchy."

Industry/Entity Type

Wedding

Colors

Designer to choose colors to be used in the design.

Requirements
Must have
• Photoshop with layers, or vector format.

Looking for that iconic poster graphic like you see in posters for classic musicals, like "Nuit Dorée," Carousel of Lanterns," or "Spindle."
Should not have
• Really don't want photos.

```html
<!DOCTYPE html>
<html lang="en">
<head>
<meta charset="utf-8">
<title>Harvest of Velmont — The New Musical</title>
<link rel="stylesheet" href="https://fonts.googleapis.com/css2?family=Raleway:wght@100;300;400&display=swap">
<style>
  :root {
    --paper: #ffffff;
    --ink-grey: #8c8c8c;
    --ink-soft: #9a9a9a;
    --wine-red: #b3121c;
    --bronze-light: #c99a6a;
    --bronze-deep: #7a4a26;
  }
  html, body {
    margin: 0;
    padding: 0;
    width: 805px;
    height: 1200px;
    overflow: hidden;
    background: var(--paper);
  }
  .poster {
    position: relative;
    width: 805px;
    height: 1200px;
    background: var(--paper);
    font-family: "Raleway", sans-serif;
    font-weight: 300;
    color: var(--ink-grey);
    overflow: hidden;
  }
  .poster p { margin: 0; }
  .presenter {
    position: absolute;
    top: 37px;
    left: 0;
    width: 100%;
    text-align: center;
    font-size: 16px;
    font-weight: 400;
    color: var(--ink-soft);
  }
  .presenter .presents { font-size: 13px; }
  .hero-figure {
    position: absolute;
    left: 266px;
    top: 146px;
    width: 310px;
    height: 380px;
    background: radial-gradient(ellipse at 50% 40%, var(--bronze-light) 0%, var(--bronze-deep) 30%, rgba(255,255,255,0) 68%);
    opacity: 0.5;
  }
  .tagline {
    position: absolute;
    top: 614px;
    left: 0;
    width: 100%;
    text-align: center;
    font-size: 17px;
    color: var(--wine-red);
    word-spacing: 4px;
  }
  .title {
    margin: 0;
    font-weight: 100;
  }
  .title span {
    position: absolute;
    line-height: 1;
    white-space: nowrap;
  }
  .title-main {
    left: 110px;
    top: 672px;
    font-size: 182px;
    letter-spacing: -3px;
    color: var(--ink-grey);
  }
  .title-link {
    left: 160px;
    top: 842px;
    font-size: 40px;
    color: var(--ink-grey);
  }
  .title-accent {
    left: 215px;
    top: 824px;
    font-size: 146px;
    letter-spacing: -3px;
    color: var(--wine-red);
  }
  .billing {
    position: absolute;
    top: 1028px;
    left: 0;
    width: 100%;
    text-align: center;
  }
  .billing .kind {
    font-size: 21px;
    font-weight: 400;
    color: var(--ink-grey);
  }
  .billing .verse {
    font-size: 15px;
    font-weight: 400;
    color: var(--wine-red);
    margin-top: 2px;
  }
  .details {
    position: absolute;
    top: 1122px;
    left: 0;
    width: 100%;
    text-align: center;
    font-size: 15px;
    line-height: 22px;
    color: var(--ink-soft);
  }
  .details .inclusion {
    margin-top: 5px;
    color: var(--wine-red);
  }
</style>
</head>
<body>
  <main class="poster">
    <p class="presenter">Lantern Table Stage <span class="presents">presents</span></p>

    <div class="hero-figure" role="img" aria-label="Warm bronze carved sculpture with outstretched arms"></div>

    <p class="tagline">Wine. Passion. Life!</p>

    <h1 class="title">
      <span class="title-main">Harvest</span>
      <span class="title-link">of</span>
      <span class="title-accent">Velmont</span>
    </h1>

    <div class="billing">
      <p class="kind">The New Musical</p>
      <p class="verse">Taste and see the goodness of the Lord!</p>
    </div>

    <div class="details">
      <p>At Saint-Anselm Catholic Church, 240 Orchard Lane</p>
      <p>Friday Night August 22 at 8pm • Tickets is $20.00</p>
      <p class="inclusion">Ticket price includes show/dinner/wine</p>
    </div>
  </main>
</body>
</html>
```